Health Coach needs a Business Card Design

Need a really modern feminine business card design for a health and lifestyle coach. Needs to use geometric shapes, muted grey/blue/green pastels and black and white - see mood board attached and logo. The client likes black and white, modern, san serif with the use of lines and possibly a shadow leaf as in the mood board. Possibly put the tag line on the back or an icon of the logo. Logo is also attached. An icon of the logo would be great too.

Target Market(s)

Women (some men) aged 30 to 50.

Industry/Entity Type

Business

Contact Information for Business Card

Marla Teveny
e-mail: hello@marlatwell.example
website: marlatwell.example
Phone: +610497258316

The tag line is "Coaching for steady wellbeing"

Font styles to use
Sans Serif

Colors
ecf7fb
cfeae6
000000
ffffff
f5f5f5

Requirements
Must have
• Black and white, logo, tag line and details
Nice to have
• Would be nice to incorporate the shadow palm.fern leaves as in the mood board and or geometric lines/shapes - see mood board. Could be either standard rectangle or would be happy with square too.
Should not have
• Flowers or decorations

```html
<!DOCTYPE html>
<html lang="en">
<head>
<meta charset="utf-8">
<title>Marla T — Business Card</title>
<link rel="stylesheet" href="https://fonts.googleapis.com/css2?family=Oswald:wght@500&family=Raleway:wght@300;400&family=Open+Sans:wght@400&display=swap">
<style>
  :root {
    --backdrop: #8a8a8a;
    --card-dark: #5b5b5b;
    --card-light: #ffffff;
    --ink: #2b2b2b;
    --ink-soft: #444444;
    --foil: #c9c9c9;
    --shadow: rgba(0, 0, 0, 0.35);
  }
  * { margin: 0; padding: 0; box-sizing: border-box; }
  html, body {
    width: 1200px;
    height: 1200px;
    overflow: hidden;
    background: var(--backdrop);
  }
  .stage {
    position: relative;
    width: 1200px;
    height: 1200px;
    display: flex;
    flex-direction: column;
    align-items: center;
    justify-content: center;
    gap: 56px;
  }
  .card {
    width: 760px;
    height: 434px;
    box-shadow: 0 14px 28px var(--shadow);
    display: flex;
    align-items: center;
    justify-content: center;
  }
  .card--front { background: var(--card-dark); }
  .card--back { background: var(--card-light); }

  .brand {
    display: flex;
    flex-direction: column;
    align-items: center;
    gap: 20px;
  }
  .brand__name {
    font-family: "Raleway", sans-serif;
    font-weight: 300;
    font-size: 58px;
    letter-spacing: 1px;
    line-height: 1;
    color: var(--foil);
  }
  .front__note {
    font-family: "Raleway", sans-serif;
    font-weight: 300;
    font-size: 17px;
    letter-spacing: 0.5px;
    color: var(--foil);
  }

  .details {
    display: flex;
    align-items: center;
    gap: 16px;
  }
  .person {
    text-align: right;
  }
  .person__name {
    font-family: "Oswald", sans-serif;
    font-weight: 500;
    font-size: 25px;
    line-height: 1.1;
    text-transform: uppercase;
    color: var(--ink);
  }
  .person__role {
    font-family: "Raleway", sans-serif;
    font-weight: 400;
    font-size: 17px;
    letter-spacing: 0.5px;
    text-transform: uppercase;
    color: var(--ink-soft);
  }
  .divider {
    width: 1.5px;
    height: 74px;
    background: var(--ink);
  }
  .contacts {
    list-style: none;
    display: flex;
    flex-direction: column;
    gap: 3px;
  }
  .contacts__item {
    display: flex;
    align-items: center;
    gap: 9px;
    font-family: "Open Sans", sans-serif;
    font-size: 16px;
    color: var(--ink);
  }
  .contacts__icon {
    width: 13px;
    height: 13px;
    fill: var(--ink);
    flex-shrink: 0;
  }
</style>
</head>
<body>
  <main class="stage">
    <section class="card card--front">
      <div class="brand">
        <span class="brand__name">Marla T</span>
        <span class="front__note">Coaching for steady wellbeing</span>
      </div>
    </section>

    <section class="card card--back">
      <div class="details">
        <div class="person">
          <div class="person__name">Marla Teveny</div>
          <div class="person__role">Director</div>
        </div>
        <div class="divider"></div>
        <ul class="contacts">
          <li class="contacts__item">
            <svg class="contacts__icon" viewBox="0 0 16 16" aria-hidden="true">
              <path d="M3.6 1.2l2.3 2.7-1.4 1.6c.9 2 2.5 3.6 4.5 4.5l1.6-1.4 2.7 2.3-1.3 2.4C7.2 13.1 2.9 8.8 1.2 3.3z"/>
            </svg>
            <span>+610497258316</span>
          </li>
          <li class="contacts__item">
            <svg class="contacts__icon" viewBox="0 0 16 16" aria-hidden="true">
              <path d="M1 3h14v1.2L8 9 1 4.2z"/>
              <path d="M1 5.6l7 4.8 7-4.8V13H1z"/>
            </svg>
            <span>hello@marlatwell.example</span>
          </li>
          <li class="contacts__item">
            <svg class="contacts__icon" viewBox="0 0 16 16" aria-hidden="true">
              <circle cx="8" cy="8" r="6.5" fill="none" stroke="#2b2b2b" stroke-width="1.4"/>
              <ellipse cx="8" cy="8" rx="2.8" ry="6.5" fill="none" stroke="#2b2b2b" stroke-width="1.2"/>
              <path d="M1.5 8h13M2.6 4.8h10.8M2.6 11.2h10.8" stroke="#2b2b2b" stroke-width="1.1" fill="none"/>
            </svg>
            <span>marlatwell.example</span>
          </li>
        </ul>
      </div>
    </section>
  </main>
</body>
</html>
```